Homepage design for personal injury lawyer

NOTE: I will not close the project until June 9th. I want to give everyone time to put in their best work.
Your task is to redesign the homepage for this site:
https://corwistlane.com/
Feel free to use any images you find on the site.
I'm deliberately leaving the description simple so that I don't limit you.
Updates
Hi everyone. I will keep the project open for a few days to leave time for designs.
Number of Pages Required
1 page
Look and feel
Each slider illustrates characteristics of the customer's brand and the style your logo design should communicate.

```html
<!DOCTYPE html>
<html lang="en">
<head>
<meta charset="utf-8">
<title>Corwist Lane — Phoenix Personal Injury Lawyers</title>
<link rel="stylesheet" href="https://fonts.googleapis.com/css2?family=Noto+Serif:wght@700&family=Open+Sans:wght@300;400;600;700&family=Oswald:wght@500&display=swap">
<style>
  :root {
    --navy: #1f2436;
    --navy-ink: #1c2336;
    --brand-blue: #3b6ea8;
    --slate: #6b6e73;
    --pill-gray: #8a8c8f;
    --orange: #f7a338;
    --panel: #f4f4f4;
    --band: #e4e4e6;
    --muted: #8a8a8a;
    --white: #ffffff;
  }
  * { box-sizing: border-box; margin: 0; padding: 0; }
  html, body { width: 1200px; height: 1076px; overflow: hidden; background: var(--white); }
  body { font-family: "Open Sans", sans-serif; color: var(--navy-ink); position: relative; }

  .site-header { position: absolute; inset: 0 0 auto 0; height: 201px; }
  .brand { position: absolute; left: 70px; top: 67px; display: flex; align-items: center; gap: 14px; }
  .brand-dot { width: 54px; height: 54px; border-radius: 50%; background: var(--brand-blue); }
  .brand-name { font-family: "Open Sans", sans-serif; font-weight: 600; font-size: 30px; color: var(--slate); letter-spacing: 1px; text-transform: uppercase; }

  .header-cta { position: absolute; right: 65px; top: 25px; display: flex; align-items: center; gap: 16px; }
  .btn-secondary { width: 145px; height: 38px; border-radius: 19px; background: var(--pill-gray); color: var(--white); font-weight: 600; font-size: 15px; display: flex; align-items: center; justify-content: center; }
  .call-pill { width: 226px; height: 55px; border-radius: 28px; background: var(--navy); color: var(--white); display: flex; flex-direction: column; align-items: center; justify-content: center; line-height: 1; }
  .call-pill small { font-size: 10.5px; font-weight: 600; margin-bottom: 4px; }
  .call-pill strong { font-size: 24px; font-weight: 700; }

  .main-nav { position: absolute; left: 565px; right: 50px; top: 104px; height: 62px; }
  .main-nav::before { content: ""; position: absolute; left: 0; right: 0; top: 0; height: 2px; background: linear-gradient(90deg, transparent, #b8b8b8 20%, #b8b8b8 80%, transparent); }
  .main-nav::after { content: ""; position: absolute; left: 0; right: 0; bottom: 0; height: 9px; background: linear-gradient(90deg, transparent, #c9c9c9 25%, #c9c9c9 75%, transparent); filter: blur(1px); }
  .main-nav ul { list-style: none; display: flex; justify-content: flex-end; gap: 28px; padding-top: 20px; padding-right: 12px; }
  .main-nav li { font-weight: 600; font-size: 14px; color: var(--navy-ink); }
  .main-nav .caret { display: inline-block; width: 0; height: 0; border-left: 3px solid transparent; border-right: 3px solid transparent; border-top: 3px solid var(--navy-ink); margin-left: 3px; vertical-align: middle; }

  .hero { position: absolute; left: 0; right: 0; top: 201px; height: 489px; background: linear-gradient(180deg, var(--band), #f6f6f7); }
  .hero-backdrop { position: absolute; left: 157px; top: 0; width: 880px; height: 489px; background: linear-gradient(120deg, #ffffff 10%, #eef0f4 45%, #e7e6ee 75%, #f1f0ec); }
  .attorney-portrait { position: absolute; left: 113px; top: -31px; width: 461px; height: 520px; background: linear-gradient(180deg, #c9c4c0 0%, #d8cfc8 35%, #2a3350 60%, #1e2640 100%); border-radius: 160px 160px 0 0; }
  .hero-panel { position: absolute; left: 574px; top: 148px; width: 626px; height: 341px; background: var(--panel); box-shadow: -4px 0 8px rgba(0,0,0,0.12); padding: 22px 0 0 38px; }
  .hero-title { font-family: "Noto Serif", serif; font-weight: 700; font-size: 40px; line-height: 1; color: var(--navy-ink); }
  .stats { display: flex; margin-top: 18px; height: 58px; }
  .stats svg { display: block; }
  .stat-num { font-family: "Noto Serif", serif; font-weight: 700; fill: var(--navy-ink); }
  .stat-label { font-family: "Oswald", sans-serif; font-weight: 500; font-size: 11px; fill: var(--navy-ink); }
  .star { fill: var(--orange); }
  .hero-lede { margin-top: 20px; font-weight: 300; font-size: 16px; line-height: 19px; color: var(--muted); width: 540px; }
  .btn-primary { margin-top: 28px; margin-left: -8px; width: 243px; height: 51px; border-radius: 26px; background: var(--orange); color: var(--white); font-family: "Noto Serif", serif; font-weight: 700; font-size: 19px; display: flex; align-items: center; justify-content: center; gap: 14px; }

  .services { position: absolute; left: 0; right: 0; top: 690px; bottom: 0; background: var(--navy); color: var(--white); }
  .services-intro { position: absolute; left: 274px; top: 43px; width: 660px; font-size: 13px; line-height: 17px; }
  .service-list { position: absolute; left: 126px; top: 123px; display: flex; gap: 124px; }
  .service { width: 224px; text-align: center; }
  .service h2 { font-family: "Noto Serif", serif; font-weight: 700; font-size: 23px; margin-bottom: 22px; }
  .service p { font-size: 13px; line-height: 16.8px; }
</style>
</head>
<body>
  <header class="site-header">
    <div class="brand">
      <span class="brand-dot"></span>
      <span class="brand-name">Corwist Lane</span>
    </div>
    <div class="header-cta">
      <a class="btn-secondary">Lorem ipsum</a>
      <a class="call-pill"><small>Call 24/7 for Free Consultation</small><strong>555-014-2290</strong></a>
    </div>
    <nav class="main-nav">
      <ul>
        <li>About Us<span class="caret"></span></li>
        <li>Case We Handle<span class="caret"></span></li>
        <li>Location<span class="caret"></span></li>
        <li>Resources<span class="caret"></span></li>
        <li>Contact Us</li>
      </ul>
    </nav>
  </header>

  <section class="hero">
    <div class="hero-backdrop"></div>
    <div class="attorney-portrait" role="img" aria-label="Portrait of a smiling attorney in a navy suit and yellow tie"></div>
    <div class="hero-panel">
      <h1 class="hero-title">Phoenix Personal<br>Injury Lawyers</h1>
      <div class="stats">
        <svg width="410" height="58" viewBox="0 0 410 58">
          <g fill="none" stroke="#1c2336" stroke-width="1.3">
            <path d="M1 1 H62 L100 57 H1 Z"/>
            <path d="M87 1 H274 L292 27 L310 57 H120 L87 10 Z"/>
            <path d="M276 1 H409 V57 H317 L276 1 Z"/>
          </g>
          <text class="stat-num" x="10" y="33" font-size="30">99<tspan font-size="16">%</tspan></text>
          <text class="stat-label" x="10" y="50">SUCCESS RATE</text>
          <text class="star" x="118" y="31" font-size="28">★★★★★</text>
          <text class="stat-label" x="126" y="50">550+ FIVE STAR ON CLIENT REVIEWS</text>
          <text class="stat-num" x="308" y="33" font-size="30"><tspan font-size="16">$</tspan>0 Fee</text>
          <text class="stat-label" x="334" y="50">UNLESS WE WIN</text>
        </svg>
      </div>
      <p class="hero-lede">Our experienced team of attorneys provides personalized legal solutions with a commitment to excellence and client satisfaction.</p>
      <a class="btn-primary">Free Consultation
        <svg width="28" height="16" viewBox="0 0 28 16" fill="none" stroke="#fff" stroke-width="2"><path d="M1 8 H26 M19 1 L26 8 L19 15"/></svg>
      </a>
    </div>
  </section>

  <section class="services">
    <p class="services-intro">Lorem ipsum dolor sit amet, consectetuer adipiscing elit, sed diam nonummy nibh euismod tincidunt ut laoreet dolore magna aliquam erat volutpat.</p>
    <div class="service-list">
      <article class="service">
        <h2>Lorem ipsum</h2>
        <p>Lorem ipsum dolor sit amet, consec-tetuer adipiscing elit, sed diam nonummy nibh euismod tincidunt ut laoreet dolore magna aliquam erat vo-lutpat. Ut wisi enim ad minim veniam, quis nostrud exerci tation ullamcorper suscipit lobortis nisl ut aliquip ex ea commodo consequat. Duis autem vel</p>
      </article>
      <article class="service">
        <h2>Lorem ipsum</h2>
        <p>Lorem ipsum dolor sit amet, consec-tetuer adipiscing elit, sed diam nonummy nibh euismod tincidunt ut laoreet dolore magna aliquam erat vo-lutpat. Ut wisi enim ad minim veniam, quis nostrud exerci tation ullamcorper suscipit lobortis nisl ut aliquip ex ea commodo consequat. Duis autem vel</p>
      </article>
      <article class="service">
        <h2>Lorem ipsum</h2>
        <p>Lorem ipsum dolor sit amet, consec-tetuer adipiscing elit, sed diam nonummy nibh euismod tincidunt ut laoreet dolore magna aliquam erat vo-lutpat. Ut wisi enim ad minim veniam, quis nostrud exerci tation ullamcorper suscipit lobortis nisl ut aliquip ex ea commodo consequat. Duis autem vel</p>
      </article>
    </div>
  </section>
</body>
</html>
```